Corvale Homes

To produce a business card design for our newly established house building and development company, We have had a logo design done please see attached, our slogan is "building your home sweet home"
Contact Information for Business Card
Adress on card needs to Read - 58 Elmsworth Lane, Holtbridge, Westmarsh WM4 4QT. Director name Dean Vascotti
Requirements
Must have
- Web adress is www.corvale-homes.co.uk
- Email address is info@corvale-homes.co.uk
- phone number 07700 900417

```html
<!DOCTYPE html>
<html lang="en">
<head>
<meta charset="utf-8">
<title>Corvale Homes – Business Card</title>
<link rel="stylesheet" href="https://fonts.googleapis.com/css2?family=Lato:wght@400;700&family=Montserrat:wght@700;800&display=swap">
<style>
  :root {
    --green: #8cc63f;
    --charcoal: #58585a;
    --roof-grey: #8e8e90;
    --white: #ffffff;
    --backdrop: #e6e6e7;
  }
  * { box-sizing: border-box; margin: 0; padding: 0; }
  html, body { width: 1200px; height: 946px; overflow: hidden; }
  body {
    background: var(--backdrop);
    font-family: "Lato", sans-serif;
    position: relative;
  }
  .card {
    position: absolute;
    left: 290px;
    width: 620px;
    height: 385px;
    overflow: hidden;
    box-shadow: 0 6px 18px rgba(0,0,0,.18);
  }
  .card--back { top: 55px; background: var(--charcoal); }
  .card--front { top: 505px; background: var(--green); }

  .wordmark {
    position: absolute;
    display: flex;
    align-items: center;
    gap: 10px;
  }
  .wordmark__mark { width: 22px; height: 22px; background: var(--green); flex: none; }
  .wordmark__name {
    font-family: "Montserrat", sans-serif;
    font-weight: 800;
    font-size: 40px;
    letter-spacing: 1px;
    color: var(--green);
    text-transform: uppercase;
    line-height: 1;
    white-space: nowrap;
  }
  .card--back .wordmark { left: 150px; top: 170px; }
  .card--front .wordmark { left: 120px; top: 272px; }
  .card--front .wordmark__name { font-size: 34px; }
  .card--front .wordmark__mark { width: 18px; height: 18px; }

  .house-shape { position: absolute; inset: 0; width: 620px; height: 385px; }

  .holder {
    position: absolute;
    left: 32px;
    top: 52px;
    color: var(--white);
    font-family: "Montserrat", sans-serif;
    text-transform: uppercase;
  }
  .holder__name { font-weight: 800; font-size: 22px; letter-spacing: .5px; }
  .holder__role { font-weight: 700; font-size: 15px; margin-top: 4px; margin-left: 18px; }

  .contact {
    position: absolute;
    right: 26px;
    top: 24px;
    text-align: right;
    color: var(--white);
    font-size: 13.5px;
    line-height: 1.55;
  }
  .contact__line { display: flex; justify-content: flex-end; align-items: center; gap: 8px; }
  .contact__icon { width: 12px; height: 12px; flex: none; }
  .address {
    position: absolute;
    right: 40px;
    top: 118px;
    text-align: right;
    color: var(--white);
    font-size: 14px;
    line-height: 1.45;
  }
</style>
</head>
<body>

<section class="card card--back" aria-label="Business card back">
  <div class="wordmark">
    <span class="wordmark__mark"></span>
    <span class="wordmark__name">Corvale Homes</span>
  </div>
</section>

<section class="card card--front" aria-label="Business card front">
  <svg class="house-shape" viewBox="0 0 620 385" aria-hidden="true">
    <polygon points="-30,300 310,150 350,168 350,95 405,95 405,190 650,295 650,420 -30,420"
             fill="var(--white)" stroke="var(--roof-grey)" stroke-width="40"
             stroke-linejoin="miter" paint-order="stroke"/>
  </svg>

  <div class="holder">
    <div class="holder__name">Dean Vascotti</div>
    <div class="holder__role">Director</div>
  </div>

  <div class="contact">
    <div class="contact__line">07700 900417
      <svg class="contact__icon" viewBox="0 0 12 12"><path d="M3 1 L5 3.5 L4 5 Q5 7 7 8 L8.5 7 L11 9 L10 11 Q4 11 1 2 Z" fill="var(--white)"/></svg>
    </div>
    <div class="contact__line">info@corvale-homes.co.uk
      <svg class="contact__icon" viewBox="0 0 12 12"><rect x="1" y="2.5" width="10" height="7" fill="none" stroke="var(--white)" stroke-width="1.2"/><path d="M1 2.5 L6 6.5 L11 2.5" fill="none" stroke="var(--white)" stroke-width="1.2"/></svg>
    </div>
    <div class="contact__line">www.corvale-homes.co.uk
      <svg class="contact__icon" viewBox="0 0 12 12"><circle cx="6" cy="6" r="5" fill="none" stroke="var(--white)" stroke-width="1.2"/><path d="M1 6 H11 M6 1 Q3 6 6 11 Q9 6 6 1" fill="none" stroke="var(--white)" stroke-width="1"/></svg>
    </div>
  </div>

  <div class="address">
    58 Elmsworth Lane,<br>
    Holtbridge,<br>
    Westmarsh<br>
    WM4 4QT.
  </div>

  <div class="wordmark">
    <span class="wordmark__mark"></span>
    <span class="wordmark__name">Corvale Homes</span>
  </div>
</section>

</body>
</html>
```